Larkmoor General Hospital School of Nursing

We need to overhaul a website we've previously used (lghsn.org) which I as administrator am no longer able to edit. There is a general history of the school which can be still used. We would like tabs for membership rosters, news and updates, scholarship information, Board of Directors information, and a chat page that is easy to use. All of our members are over 70 years of age, so simplicity is important.

```html
<!DOCTYPE html>
<html lang="en">
<head>
<meta charset="UTF-8">
<title>Get a Membership · Larkmoor General Hospital School of Nursing</title>
<link rel="stylesheet" href="https://fonts.googleapis.com/css2?family=DM+Serif+Display&family=Libre+Caslon+Text:wght@700&family=Jost:wght@300&display=swap">
<style>
  :root {
    --brand-blue: #00449a;
    --brand-yellow: #fdcd62;
    --required-red: #d0202a;
    --paper: #ffffff;
    --photo-light: #d9d9d9;
    --photo-dark: #6f6f6f;
  }
  * { box-sizing: border-box; margin: 0; padding: 0; }
  html, body { width: 1200px; height: 675px; overflow: hidden; background: var(--paper); }
  .page { position: relative; width: 1200px; height: 675px; overflow: hidden; }

  .site-header {
    position: absolute; left: 0; top: 0; width: 1200px; height: 150px;
    background: var(--brand-blue);
  }
  .nav-link {
    position: absolute; top: 100px;
    font-family: "Libre Caslon Text", serif; font-weight: 700; font-size: 18px;
    color: var(--paper); text-decoration: none; white-space: nowrap;
  }
  .nav-about { left: 95px; }
  .nav-portal { left: 276px; }
  .nav-contact { left: 748px; }
  .nav-news { left: 936px; }

  .brand {
    position: absolute; left: 525px; top: 16px; width: 150px;
    display: flex; flex-direction: column; align-items: center; gap: 8px;
  }
  .brand-dot { width: 54px; height: 54px; border-radius: 50%; background: var(--brand-yellow); }
  .brand-name {
    font-family: "Libre Caslon Text", serif; font-weight: 700; font-size: 11px;
    line-height: 1.3; text-align: center; color: var(--brand-yellow);
  }

  .page-title {
    position: absolute; left: 46px; top: 156px;
    font-family: "DM Serif Display", serif; font-weight: 400; font-size: 70px;
    line-height: 1; letter-spacing: 0.3px; color: var(--brand-blue); white-space: nowrap;
  }

  .field-label {
    position: absolute;
    font-family: "Libre Caslon Text", serif; font-weight: 700; font-size: 16px;
    color: var(--brand-blue); white-space: nowrap;
  }
  .required { color: var(--required-red); }
  .field-input {
    position: absolute; height: 35px;
    border: 4px solid var(--brand-blue); background: var(--paper);
  }
  .label-first { left: 99px; top: 272px; }
  .label-last { left: 300px; top: 272px; }
  .label-year { left: 99px; top: 347px; }
  .label-email { left: 298px; top: 347px; }
  .input-first { left: 95px; top: 296px; width: 172px; }
  .input-last { left: 296px; top: 296px; width: 172px; }
  .input-year { left: 95px; top: 369px; width: 172px; }
  .input-email { left: 298px; top: 369px; width: 172px; }

  .section-title {
    position: absolute; left: 68px; top: 426px;
    font-family: "DM Serif Display", serif; font-weight: 400; font-size: 40px; letter-spacing: 0.5px;
    color: var(--brand-blue); white-space: nowrap;
  }

  .pill-button {
    position: absolute; border-radius: 30px; background: var(--brand-blue);
    color: var(--paper); font-family: "Libre Caslon Text", serif; font-weight: 700; font-size: 13.5px;
    text-decoration: none;
    display: flex; align-items: center; justify-content: center; white-space: nowrap;
  }
  .btn-yearly { left: 100px; top: 503px; width: 146px; height: 58px; }
  .btn-donate { left: 316px; top: 501px; width: 152px; height: 60px; padding-bottom: 6px; }

  .hero-photo {
    position: absolute; left: 615px; top: 194px; width: 571px; height: 386px;
    background: linear-gradient(160deg, var(--photo-light) 0%, #a9a9a9 45%, var(--photo-dark) 70%, #e6e6e6 100%);
  }
  .intro-bubble {
    position: absolute; left: 658px; top: 340px; width: 501px; height: 115px;
    border-radius: 58px; background: var(--brand-yellow);
    display: flex; align-items: center; justify-content: center; text-align: center;
    font-family: "Jost", sans-serif; font-weight: 300; font-size: 19px; line-height: 1.3;
    color: var(--brand-blue); padding: 0 30px;
  }
</style>
</head>
<body>
<div class="page">
  <header class="site-header">
    <a class="nav-link nav-about" href="#">About Us</a>
    <a class="nav-link nav-portal" href="#">Member Portal</a>
    <div class="brand">
      <span class="brand-dot"></span>
      <span class="brand-name">Larkmoor General Hospital<br>School of Nursing</span>
    </div>
    <a class="nav-link nav-contact" href="#">Contact Us</a>
    <a class="nav-link nav-news" href="#">News &amp; Updates</a>
  </header>

  <h1 class="page-title">get a membersip</h1>

  <label class="field-label label-first">first name<span class="required">*</span></label>
  <div class="field-input input-first"></div>
  <label class="field-label label-last">last name<span class="required">*</span></label>
  <div class="field-input input-last"></div>
  <label class="field-label label-year">graduation year</label>
  <div class="field-input input-year"></div>
  <label class="field-label label-email">email<span class="required">*</span></label>
  <div class="field-input input-email"></div>

  <h2 class="section-title">choose membership type</h2>
  <a class="pill-button btn-yearly" href="#">yearly membership</a>
  <a class="pill-button btn-donate" href="#">donate now</a>

  <div class="hero-photo" role="img" aria-label="Black and white photograph of three nurses in caps beside a hospital bed"></div>
  <p class="intro-bubble">We are an association of more than 750 graduates of the Larkmoor General Hospital School of Nursing, formerly located in Larkmoor’s East Quarter.</p>
</div>
</body>
</html>
```